Redesign Craft Brewing Recipe Website

Originally built with Bootstrap just to get the site going, I am seeking a complete redesign of the sites home page and recipe page. I am an experienced web developer with no graphic background, initially just looking for psd mocks.

I prefer styles that are clean and modern, and would prefer anything that is fun, engaging, and has an organic feel to it. I currently have a cartoon rabbit as a logo, but it needs some modification/tweaking, so any help in that area would be great as well.

Current site:
http://kettlefinch.hostgridapps.net/

Current launch page/logo:
http://www.kettlefinch.com/

I like the overall layout of the elements currently, but the design sucks.
Updates

The launch page is at the following URL

Reason: Still looking for a more modern design. Designs received so far are too similar to the original.

My site is content based and does not contain images or products. Your design should not consist of large images.

Reason: The website has very little images, so the designs need to be more text and content based. The header needs to be very small and should not contain an ad rotater.

Target Market(s)

Home brewers, Craft brewers, Microbreweries, Brewpubs

Requirements
Must have
• Web 2.0 Look and Feel, Fun, Hip, Focus on content
Should not have
• A large photo as a header

```html
<!DOCTYPE html>
<html lang="en">
<head>
<meta charset="utf-8">
<title>KettleFinch – Recipes</title>
<link href="https://fonts.googleapis.com/css2?family=Open+Sans:wght@400;600;700;800&display=swap" rel="stylesheet">
<style>
:root{
  --ink:#2b2b2b;
  --bar:#2e2e2e;
  --bar-dark:#1f1f1f;
  --amber:#f5b400;
  --amber-deep:#e49a00;
  --page:#ececec;
  --panel:#f6f6f6;
  --card:#ffffff;
  --line:#dcdcdc;
  --muted:#8a8a8a;
  --title:#8a4a12;
  --link:#2f6fb0;
  --green:#6aa51f;
  --orange:#f08a00;
  --navy:#173a66;
  --charcoal:#2a2a2a;
  --yellow:#f7c600;
}
*{box-sizing:border-box;margin:0;padding:0}
html,body{width:705px;height:1200px;overflow:hidden}
body{font-family:"Open Sans",Arial,sans-serif;background:var(--page);color:var(--ink);position:relative}

.topbar{position:absolute;left:0;top:0;width:705px;height:40px;background:linear-gradient(#3a3a3a,var(--bar-dark))}
.brand{position:absolute;left:22px;top:8px;font-size:19px;font-weight:800;color:#fff;letter-spacing:.5px;line-height:24px}
.nav{position:absolute;right:22px;top:9px;display:flex;gap:22px;align-items:center;font-size:11px;color:#ddd;line-height:20px}
.nav .login{background:#111;border:1px solid #555;border-radius:3px;padding:0 10px;color:#fff}

.intro-band{position:absolute;left:0;top:40px;width:705px;height:92px;background:linear-gradient(var(--amber),var(--amber-deep))}
.intro{position:absolute;left:30px;top:54px;width:645px;height:64px;background:rgba(25,25,25,.88);border-radius:3px;padding:10px 14px;color:#fff;display:flex;align-items:center;gap:16px}
.intro-head{width:170px;flex:none}
.intro-head h2{font-size:14px;font-weight:700;line-height:18px}
.intro-head h3{font-size:10px;font-weight:600;line-height:14px}
.intro p{flex:1;font-size:8px;line-height:12px;color:#bbb}
.intro .btns{display:flex;gap:6px;flex:none}

.tag{font-size:8px;line-height:10px;color:#fff;padding:4px 8px;border-radius:2px;display:inline-block;white-space:nowrap}
.tag.green{background:var(--green)}.tag.dark{background:#3a3a3a}.tag.orange{background:var(--orange)}.tag.red{background:#c0201a}

.content{position:absolute;left:30px;top:132px;width:645px;height:1031px;background:var(--panel)}

.sidebar{position:absolute;left:47px;top:152px;width:200px;height:474px;background:var(--card);border:1px solid var(--line);border-radius:3px;padding:12px}
.search{display:flex;height:18px}
.search span{flex:1;border:1px solid var(--line);font-size:8px;line-height:10px;color:var(--muted);padding:3px 5px}
.search b{width:18px;background:var(--orange)}
.sidebar h4{font-size:9px;font-weight:700;margin:16px 0 5px;letter-spacing:.3px;line-height:12px}
.opt{font-size:8px;color:#555;display:flex;align-items:center;gap:5px;height:13px;white-space:nowrap}
.opt::before{content:"";width:7px;height:7px;border:1px solid #bbb;display:block;flex:none}
.styles{position:relative}
.styles .track{position:absolute;right:4px;top:0;width:2px;height:140px;background:#ddd}
.styles .knob{position:absolute;right:1px;top:20px;width:8px;height:8px;border-radius:50%;background:#333}

.card{position:absolute;left:266px;width:388px;height:200px;background:var(--card);border:1px solid var(--line);border-radius:3px}
.thumb{position:absolute;left:14px;top:14px;width:70px;height:60px}
.card h3{position:absolute;left:96px;top:12px;font-size:11px;line-height:14px;font-weight:700;color:var(--title)}
.card p{position:absolute;left:96px;top:28px;width:270px;font-size:7px;line-height:10px;color:var(--muted)}
.card .by{position:absolute;left:96px;top:50px;font-size:7px;line-height:10px;color:#555}
.card .tags{position:absolute;left:96px;top:64px;display:flex;gap:5px}
.stats{position:absolute;left:34px;bottom:22px;display:flex;gap:10px;align-items:center}
.stat{width:40px;height:40px;border-radius:50%;border:1px solid #ccc;background:#fafafa;display:flex;flex-direction:column;align-items:center;justify-content:center;font-size:8px;color:#555;line-height:10px}
.stat small{font-size:6px;line-height:8px;color:var(--muted)}
.stat.big{width:46px;height:46px;border:none;color:#fff;font-weight:700}
.stat.big small{color:#fff}

.footer{position:absolute;left:0;top:1163px;width:705px;height:37px;background:var(--bar)}
.footer p{position:absolute;left:20px;top:13px;font-size:8px;line-height:11px;color:#aaa}
.social{position:absolute;right:20px;top:11px;display:flex;gap:4px}
.social i{width:14px;height:14px;border-radius:50%;background:#ddd;display:block}
</style>
</head>
<body>
<header class="topbar">
  <div class="brand">KETTLEFINCH</div>
  <nav class="nav"><span>Main</span><span>About</span><span>Recipes</span><span class="login">Login</span></nav>
</header>

<section class="intro-band"></section>
<section class="intro">
  <div class="intro-head">
    <h2>Mauris vel lacus vitae</h2>
    <h3>felis vestibulum volutpat</h3>
  </div>
  <p>Nam tempus dolor vitae urna. Mauris vitae felis eu ipsum hendrerit dictum, a tempor felis ac ligula varius. Sed ac est a lorem commodo, nec gravida metus.</p>
  <div class="btns"><span class="tag green">Extract</span><span class="tag dark">Sweet Mead</span></div>
</section>

<main class="content"></main>

<aside class="sidebar">
  <div class="search"><span>Search</span><b></b></div>
  <h4>BREWING</h4>
  <div class="opt">Extract</div><div class="opt">Partial Mash</div><div class="opt">All Grain</div>
  <h4>STYLES</h4>
  <div class="styles">
    <div class="track"></div><div class="knob"></div>
    <div class="opt">American Amber Ale</div><div class="opt">American Barleywine</div>
    <div class="opt">American Brown Ale</div><div class="opt">American IPA</div>
    <div class="opt">American Pale Ale</div><div class="opt">American Stout</div>
    <div class="opt">American Wheat or Rye Beer</div><div class="opt">Applewine</div>
  </div>
  <h4>MATCH MAKER</h4>
  <div class="opt">Boil Size</div>
</aside>

<article class="card" style="top:152px">
  <div class="thumb" role="img" aria-label="Photo of a glass of mead" style="background:linear-gradient(#6a3a12,#c58a2a)"></div>
  <h3>Oak Bastard Sweet Mead</h3>
  <p>Lorem ipsum dolor sit amet, consectetur adipiscing elit, sed do eiusmod tempor incididunt ut labore.</p>
  <div class="by">created by <span style="color:var(--link)">Dana Hollis</span></div>
  <div class="tags"><span class="tag green">Extract</span><span class="tag dark">Sweet Mead</span></div>
  <div class="stats"><div class="stat">2.24%<small>abv</small></div><div class="stat">24<small>ibu</small></div><div class="stat">1.086<small>fg</small></div><div class="stat">1.022<small>og</small></div><div class="stat big" style="background:var(--orange)">6<small>srm</small></div></div>
</article>

<article class="card" style="top:382px">
  <div class="thumb" role="img" aria-label="Photo of a pint of Belgian ale" style="background:linear-gradient(#3a2a1a,#b36a1e)"></div>
  <h3>Venom Belgian Specialty Ale</h3>
  <p>Lorem ipsum dolor sit amet, consectetur adipiscing elit, sed do eiusmod tempor incididunt ut labore.</p>
  <div class="by">created by <span style="color:var(--link)">Dana Hollis</span></div>
  <div class="tags"><span class="tag orange">PartialMash</span><span class="tag dark">Belgian Specialty Ale</span></div>
  <div class="stats"><div class="stat">2.24%<small>abv</small></div><div class="stat">24<small>ibu</small></div><div class="stat">1.086<small>fg</small></div><div class="stat">1.022<small>og</small></div><div class="stat big" style="background:var(--navy)">6<small>srm</small></div></div>
</article>

<article class="card" style="top:612px">
  <div class="thumb" role="img" aria-label="Photo of tripel beer glasses" style="background:linear-gradient(#e8c25a,#9a6a1a)"></div>
  <h3>Honeysucker Belgian Tripel</h3>
  <p>Lorem ipsum dolor sit amet, consectetur adipiscing elit, sed do eiusmod tempor incididunt ut labore.</p>
  <div class="by">created by <span style="color:var(--link)">Dana Hollis</span></div>
  <div class="tags"><span class="tag green">Extract</span><span class="tag dark">Belgian Tripel</span></div>
  <div class="stats"><div class="stat">2.24%<small>abv</small></div><div class="stat">24<small>ibu</small></div><div class="stat">1.086<small>fg</small></div><div class="stat">1.022<small>og</small></div><div class="stat big" style="background:var(--charcoal)">6<small>srm</small></div></div>
</article>

<article class="card" style="top:842px">
  <div class="thumb" role="img" aria-label="Photo of a pilsner glass" style="background:linear-gradient(#f2d26a,#a07018)"></div>
  <h3>Hooker German Pilsner (Pils)</h3>
  <p>Lorem ipsum dolor sit amet, consectetur adipiscing elit, sed do eiusmod tempor incididunt ut labore.</p>
  <div class="by">created by <span style="color:var(--link)">Dana Hollis</span></div>
  <div class="tags"><span class="tag red">AllGrain</span><span class="tag dark">German Pilsner (Pils)</span></div>
  <div class="stats"><div class="stat">2.24%<small>abv</small></div><div class="stat">24<small>ibu</small></div><div class="stat">1.086<small>fg</small></div><div class="stat">1.022<small>og</small></div><div class="stat big" style="background:var(--yellow)">6<small>srm</small></div></div>
</article>

<footer class="footer">
  <p>© 2013 Company name · All rights reserved · Terms of Use</p>
  <div class="social"><i></i><i></i><i></i><i></i><i></i></div>
</footer>
</body>
</html>
```